Website design for Harbor Bolts. ( Lock company)

Harbor Bolts is a New York Based Company that manufactures a variety of high quality Locks which sell worldwide.

Our website: We need a 'face' on the Internet , a website that tells you who we are and what we do - 'An Identity'.

it is not an eCommerce website . the website is to show customers and potential distributers who we are and what we manufacture ( so they come away with a great impression of our company and our products) see www.quarrelwheel.com

First glance impression: We are Professional; are locks are strong,and reliable. and we are ready to compete with other major Lock companies

Content: for starters the site will contain general information and background about our company (our story), were to buy our products, contact information, and display images of our Locks (and of course all the classic links including to all the legal and technical information). as time goes on we will add more features to the website i.e. Products, Videos blogs etc.

although at first there will not be that much content on the website - it should not look empty (it should be simple and clear but not empty) it should look and feel like a full fledged professional website (not a template)

Inspiration: here are a few sites which have the feel we are looking for:

General tone - quarrelwheel.com bramhold.com (black is good - But not a must )

Simplicity, clarity - coldvane.com panwright.com

the widescreen Image look - http://www.pagecritter.com/demo/58261.html

we are considering perhaps having wide HQ images of Lion(s) in the background (but without the felling that it is a zoo or safari website) - it is not a must, its just an idea .

perhaps (if you find it looks good ) use a bit of that metal or chrome look to give it it a strong smooth feel (however it should not look like a dark prison)

We do not currently have a Logo ( if you feel you can design one that fits the above company description - we would love to see if it can work for us) We can talk about additional funds for the logo during this project.

Our working slogan is : Harbor Bolts - "Keeper of your Ground"

for your convenience we have attached a few images of the type of locks we sell

We are looking to collaborate with you throughout the project. We have ideas and visions we want implemented and we will help you along the way. So we can create the perfect website.

Thank you.

```html
<!DOCTYPE html>
<html lang="en">
<head>
<meta charset="utf-8">
<title>Harbor Bolts – Keeper of your Ground</title>
<link rel="stylesheet" href="https://fonts.googleapis.com/css2?family=Open+Sans:wght@400;600;700&family=Roboto:wght@700;900&display=swap">
<style>
  :root {
    --ink-dark: #1b1a19;
    --hero-deep: #1d1814;
    --hero-mid: #3a3029;
    --hero-warm: #4a3d33;
    --bar: #222222;
    --bar-edge: #2e2e2e;
    --white: #ffffff;
    --accent-red: #a3050b;
    --page-grey: #e6e8eb;
    --panel: #efefef;
    --panel-line: #d9d9d9;
    --text: #1d1d1d;
    --muted: #6b6b6b;
    --button: #1f8fdb;
    --button-dark: #1a78ba;
  }
  * { box-sizing: border-box; margin: 0; padding: 0; }
  html, body { width: 1200px; height: 900px; overflow: hidden; }
  body {
    position: relative;
    background: var(--page-grey);
    font-family: "Open Sans", Arial, sans-serif;
    color: var(--text);
  }

  /* Hero */
  .hero {
    position: absolute; left: 0; top: 0; width: 1200px; height: 600px;
    overflow: hidden;
  }
  .hero-photo {
    position: absolute; inset: 0;
    background:
      radial-gradient(ellipse at 85% 15%, rgba(110,95,80,.55), transparent 45%),
      radial-gradient(ellipse at 20% 70%, rgba(70,55,45,.6), transparent 55%),
      linear-gradient(160deg, var(--hero-warm) 0%, var(--hero-mid) 35%, var(--hero-deep) 100%);
  }
  .hero-shade { position: absolute; inset: 0; background: rgba(0,0,0,.28); }

  .site-header {
    position: absolute; left: 0; top: 0; width: 100%; height: 90px;
  }
  .brand {
    position: absolute; left: 140px; top: 20px;
    display: flex; align-items: center; gap: 12px;
  }
  .brand-mark {
    width: 22px; height: 22px; border-radius: 50%; background: var(--white);
  }
  .brand-name {
    font-weight: 700; font-size: 27px; letter-spacing: .5px; color: var(--white);
    text-transform: uppercase; line-height: 1;
  }
  .brand-tagline {
    position: absolute; left: 225px; top: 58px;
    font-size: 11px; color: var(--white); letter-spacing: .4px; text-transform: uppercase;
  }
  .main-nav {
    position: absolute; right: 140px; top: 24px;
    display: flex; gap: 20px;
  }
  .main-nav a, .sticky-nav a {
    color: var(--white); text-decoration: none; font-size: 17px; text-transform: uppercase;
  }

  .hero-lock {
    position: absolute; left: 521px; top: 112px; width: 156px; height: 156px;
  }
  .hero-title {
    position: absolute; left: 0; top: 305px; width: 100%; text-align: center;
    font-family: "Roboto", Arial, sans-serif; font-weight: 900;
    font-size: 104px; line-height: 1; letter-spacing: 1px; color: var(--white);
  }
  .hero-title .accent { color: var(--accent-red); }
  .hero-slogan {
    position: absolute; left: 0; top: 422px; width: 100%; text-align: center;
    font-family: "Roboto", Arial, sans-serif; font-weight: 700;
    font-size: 62px; line-height: 1; color: var(--white); text-transform: uppercase;
  }
  .slider-arrow {
    position: absolute; top: 280px; width: 42px; height: 46px;
    background: rgba(0,0,0,.35);
    display: flex; align-items: center; justify-content: center;
  }
  .slider-arrow.prev { left: 118px; }
  .slider-arrow.next { left: 1042px; }

  /* Sticky bar */
  .sticky-bar {
    position: absolute; left: 0; top: 600px; width: 1200px; height: 48px;
    background: var(--bar); border-bottom: 2px solid var(--bar-edge);
  }
  .sticky-bar .brand { left: 245px; top: 13px; gap: 10px; }
  .sticky-bar .brand-mark { width: 16px; height: 16px; }
  .sticky-bar .brand-name { font-size: 19px; }
  .sticky-nav {
    position: absolute; right: 150px; top: 12px; display: flex; gap: 20px;
  }

  /* Welcome */
  .welcome {
    position: absolute; left: 190px; top: 680px; width: 832px; height: 220px;
    background: var(--panel); border-top: 1px solid var(--panel-line);
  }
  .welcome h1 {
    position: absolute; left: 28px; top: 22px;
    font-size: 17px; font-weight: 600; color: var(--text);
  }
  .welcome p {
    position: absolute; left: 28px; top: 56px;
    font-size: 11px; color: var(--muted);
  }
  .purchase-button {
    position: absolute; left: 648px; top: 26px; width: 160px; height: 58px;
    background: var(--button); border: 1px solid var(--button-dark); border-radius: 2px;
    color: var(--white); text-decoration: none;
    display: flex; align-items: flex-start; gap: 8px; padding: 10px 10px;
  }
  .purchase-button .label { font-size: 14px; line-height: 1.2; }
  .purchase-button .sub { display: block; font-size: 10px; opacity: .9; }
</style>
</head>
<body>
  <section class="hero">
    <div class="hero-photo" role="img" aria-label="Wide close-up photograph of a lion's dark mane fur"></div>
    <div class="hero-shade"></div>

    <header class="site-header">
      <div class="brand">
        <span class="brand-mark"></span>
        <span class="brand-name">Harbor Bolts</span>
      </div>
      <span class="brand-tagline">Best lock ever</span>
      <nav class="main-nav">
        <a href="#">Home</a><a href="#">About</a><a href="#">Product</a>
        <a href="#">Testimonials</a><a href="#">Online Shop</a><a href="#">Contact</a>
      </nav>
    </header>

    <svg class="hero-lock" viewBox="0 0 156 156" aria-hidden="true">
      <circle cx="78" cy="78" r="74" fill="none" stroke="#ffffff" stroke-width="5"/>
      <path d="M60 72 V58 a18 18 0 0 1 36 0 V72" fill="none" stroke="#ffffff" stroke-width="8"/>
      <rect x="50" y="70" width="56" height="44" rx="6" fill="#ffffff"/>
      <circle cx="78" cy="88" r="6" fill="#1d1814"/>
      <rect x="75" y="90" width="6" height="13" fill="#1d1814"/>
    </svg>

    <h2 class="hero-title">HARBOR<span class="accent">BOLTS</span></h2>
    <p class="hero-slogan">Keeper of your Ground</p>

    <a class="slider-arrow prev" href="#" aria-label="Previous slide">
      <svg width="12" height="16" viewBox="0 0 12 16"><path d="M9 2 L3 8 L9 14" fill="none" stroke="#fff" stroke-width="2.5"/></svg>
    </a>
    <a class="slider-arrow next" href="#" aria-label="Next slide">
      <svg width="12" height="16" viewBox="0 0 12 16"><path d="M3 2 L9 8 L3 14" fill="none" stroke="#fff" stroke-width="2.5"/></svg>
    </a>
  </section>

  <div class="sticky-bar">
    <div class="brand">
      <span class="brand-mark"></span>
      <span class="brand-name">Harbor Bolts</span>
    </div>
    <nav class="sticky-nav">
      <a href="#">Home</a><a href="#">About</a><a href="#">Product</a>
      <a href="#">Testimonials</a><a href="#">Online Shop</a><a href="#">Contact</a>
    </nav>
  </div>

  <section class="welcome">
    <h1>Welcome to harbor bolts official website !</h1>
    <p>Best place to shop your locks , blahblahblah...</p>
    <a class="purchase-button" href="#">
      <svg width="22" height="20" viewBox="0 0 22 20" aria-hidden="true">
        <path d="M1 2 H5 L8 13 H18 L21 5 H6" fill="none" stroke="#fff" stroke-width="2"/>
        <circle cx="9" cy="17" r="2" fill="#fff"/><circle cx="17" cy="17" r="2" fill="#fff"/>
      </svg>
      <span class="label">Purchase Now!<span class="sub">Give safety to your home</span></span>
    </a>
  </section>
</body>
</html>
```